Personal Development Business needs a Business Card Design Project

We need a buiness card design for a new Personal Development business based in S. NSW in Australia called "Willow Path Onward. Our target market is to women who are looking to re-enter the workforce, or already be in the workforce at the middle management level. As a result of consultations their outcomes will be, but not exclusive to: increased confidence, increased self esteem and self awareness, work-life balance, time management, positive thinking.
Behind the scenes of coaching and mentoring will be a spiritual "bent".
Anticipate a beautiful candle as a possible background - showing success and shining - see attachment which came off Pixelmarket. Colours - Unsure until I see something that "grabs my attention". Not esoteric fluffy design but something that suggests safe, professional, supportive of personal journey without being too corporate.
Look forward to what you come up with.
Target Market(s)
Some designers have been requesting various bits of information.
Personal information. See attachment.
Two-sided please.
Gold lines at all four edges.
Many thanks
Ruth
Industry/Entity Type
Business
Look and feel
Each slider illustrates characteristics of the customer's brand and the style your logo design should communicate.

```html
<!DOCTYPE html>
<html lang="en">
<head>
<meta charset="utf-8">
<title>Willow Path Onward – Business Card</title>
<link href="https://fonts.googleapis.com/css2?family=Pinyon+Script&family=Arimo:wght@400;700&display=swap" rel="stylesheet">
<style>
  :root {
    --page-bg: #f6f6f6;
    --card-bg: #f1f1f1;
    --card-bg-light: #fafafa;
    --gold: #b39a2c;
    --gold-deep: #9c8422;
    --gold-soft: #d9ca8c;
    --ink: #5a5a5a;
    --ink-soft: #8a8a8a;
    --script-light: #c4c4c4;
    --white: #ffffff;
  }
  * { box-sizing: border-box; margin: 0; padding: 0; }
  html, body { width: 1200px; height: 729px; overflow: hidden; }
  body {
    background: var(--page-bg);
    font-family: "Arimo", Arial, sans-serif;
    position: relative;
  }
  .card {
    position: absolute;
    top: 200px;
    width: 490px;
    height: 272px;
    border: 1.5px solid var(--gold);
    background: linear-gradient(160deg, var(--card-bg-light), var(--card-bg));
    overflow: hidden;
  }
  .card--front { left: 80px; }
  .card--back { left: 630px; }

  /* Front */
  .front__tagline {
    position: absolute;
    left: 20px;
    top: 92px;
    font-family: "Pinyon Script", cursive;
    font-size: 42px;
    color: var(--gold);
    white-space: nowrap;
  }
  .front__service {
    position: absolute;
    left: 166px;
    bottom: 10px;
    font-size: 13px;
    font-weight: 700;
    color: var(--gold);
    letter-spacing: -0.2px;
  }

  /* Back */
  .back__name {
    position: absolute;
    left: 20px;
    top: 14px;
    font-size: 16px;
    color: var(--gold);
  }
  .back__credentials {
    position: absolute;
    left: 20px;
    top: 36px;
    list-style: none;
    font-size: 6px;
    line-height: 8px;
    color: var(--ink);
  }
  .back__tagline {
    position: absolute;
    right: 10px;
    top: 52px;
    font-family: "Pinyon Script", cursive;
    font-size: 36px;
    color: var(--script-light);
    white-space: nowrap;
  }
  .back__band {
    position: absolute;
    left: 0;
    right: 0;
    top: 130px;
    height: 18px;
    background: linear-gradient(90deg, var(--white) 0%, var(--gold-soft) 25%, var(--gold) 60%, var(--gold-deep) 100%);
    display: flex;
    align-items: center;
    justify-content: space-between;
    padding: 0 10px 0 14px;
    font-size: 12.5px;
    color: var(--white);
  }
  .back__band .band__item--first { color: var(--ink-soft); }
  .back__contact {
    position: absolute;
    left: 20px;
    top: 184px;
    list-style: none;
    font-size: 11px;
    line-height: 15px;
    color: var(--ink);
  }
  .contact__key {
    display: inline-block;
    width: 16px;
    color: var(--gold);
  }
</style>
</head>
<body>

  <section class="card card--front" aria-label="Card front">
    <p class="front__tagline">Willow Path Onward</p>
    <p class="front__service">Personal Development</p>
  </section>

  <section class="card card--back" aria-label="Card back">
    <h1 class="back__name">Ruth Calder</h1>
    <ul class="back__credentials">
      <li>Grad Dip Management</li>
      <li>BA Social History</li>
      <li>Master Practitioner</li>
    </ul>
    <p class="back__tagline">Willow Path Onward</p>
    <div class="back__band">
      <span class="band__item band__item--first">Self Awareness</span>
      <span class="band__item">Confidence</span>
      <span class="band__item">Work-Life Balance</span>
    </div>
    <ul class="back__contact">
      <li><span class="contact__key">M</span>0400 118 526</li>
      <li><span class="contact__key">E</span>ruthatwillow@treeline.com.au</li>
      <li><span class="contact__key">W</span>willowpathonward.com.au</li>
    </ul>
  </section>

</body>
</html>
```